With over 10 years of experience as the president of Brightpath Access Group, LLC, we provide training and consulting services on various accessibility laws and standards, such as the ADA, Section 504, Fair Housing Act, and ANSI A117.1. My company specializes in helping agencies and commercial entities achieve compliance and create an inclusive environment for all customers.

In my role, I conduct ADA self-assessments, consult on transition plans, and deliver training on accessible design, program access, and reasonable accommodations. I use and develop skills such as public speaking, project management, and strategic problem-solving. I value collaboration, innovation, and diversity, and I strive to empower and support my clients and team members in reaching their accessibility goals.

https://brightpathaccessgroup.example/

Target Market(s)

See web site: https://brightpathaccessgroup.example/ or linked in for more language: https://www.linkedin.com/in/tom-hollis-572048163/

Industry/Entity Type

Education and consultative

Other font styles liked:
• Times New Roman

Requirements
Must have
• Specializes in ADA surveys, litigation assistance, construction consultation and transition plans.
Nice to have
• The photos I shared
Should not have
• Any other pictures or negative items

```html
<!DOCTYPE html>
<html lang="en">
<head>
<meta charset="utf-8">
<title>Brightpath Access Group, LLC – Flyer</title>
<link rel="stylesheet" href="https://fonts.googleapis.com/css2?family=Montserrat:wght@400;500;600;700;800&family=Oswald:wght@500&family=Great+Vibes&display=swap">
<style>
  :root{
    --orange:#f28c1e;
    --orange-deep:#ef7d17;
    --orange-light:#f6a531;
    --blue:#1c8fd0;
    --blue-deep:#1878c4;
    --white:#ffffff;
    --ink:#2b2b2b;
    --pale:#eeeeee;
  }
  *{box-sizing:border-box;margin:0;padding:0}
  html,body{width:1000px;height:1200px;overflow:hidden;background:#ffffff}
  body{font-family:"Montserrat",Arial,sans-serif;color:var(--ink)}
  .flyer{position:relative;width:1000px;height:1200px;overflow:hidden;background:var(--white)}
  .abs{position:absolute}
  .shapes{position:absolute;inset:0}

  .brand-name{left:73px;top:26px;font-size:26px;font-weight:700;color:var(--orange);letter-spacing:.2px}
  .brand-tag{left:73px;top:64px;width:425px;height:28px;background:var(--orange);color:var(--white);
    font-size:14.5px;font-weight:500;display:flex;align-items:center;justify-content:center}
  .site{left:631px;top:30px;font-size:17px;color:var(--white);font-weight:400}
  .site b{font-weight:700}

  .photo{position:absolute}
  .hero{left:0;top:0;width:1000px;height:440px;
    background:linear-gradient(120deg,#e9e4dc 0%,#cfc7ba 35%,#8c7c68 60%,#5e7a3f 85%,#8fae5c 100%);
    clip-path:polygon(0 115px,540px 115px,540px 68px,1000px 68px,1000px 440px,0 440px)}
  .badge-spot{left:742px;top:305px;width:96px;height:96px;border-radius:50%;background:var(--white);opacity:.9}

  .headline{left:73px;top:428px;font-size:26.5px;font-weight:800;color:var(--white);line-height:33px;white-space:nowrap}
  .call{left:73px;top:546px;font-size:20px;font-weight:800;color:var(--white);display:flex;align-items:center;gap:8px;line-height:24px}
  .phone-pill{left:73px;top:574px;width:362px;height:47px;background:var(--blue);border-radius:0 24px 24px 0;
    display:flex;align-items:center}
  .phone-pill .ring{width:54px;height:54px;margin-left:-4px;border-radius:50%;background:var(--orange);
    border:4px solid var(--white);display:flex;align-items:center;justify-content:center}
  .phone-pill .num{margin-left:14px;font-size:33px;font-weight:800;color:var(--white)}

  .exp-box{left:781px;top:469px;width:176px;height:93px;border:1.5px solid var(--white)}
  .exp-years{left:795px;top:470px;font-family:"Oswald",Arial,sans-serif;font-size:46px;color:var(--white);line-height:56px}
  .exp-of{left:795px;top:526px;width:148px;height:23px;background:var(--blue);color:var(--white);
    font-size:13.5px;font-weight:700;letter-spacing:.8px;display:flex;align-items:center;justify-content:center}
  .exp-over{left:660px;top:470px;font-family:"Great Vibes",cursive;font-size:86px;color:var(--white);line-height:100px}

  .site-photo{border-radius:4px}
  .p-team{left:72px;top:636px;width:226px;height:290px;background:linear-gradient(160deg,#3f6fae,#e2dbd0 55%,#f1efe9)}
  .p-law{left:306px;top:636px;width:227px;height:119px;background:linear-gradient(120deg,#2e4a78,#6d5038 70%,#4a2c1c)}
  .p-access{left:306px;top:763px;width:227px;height:163px;background:linear-gradient(150deg,#5a86b8,#a9c3de 60%,#dfe7ef)}

  .intro{left:90px;top:958px;width:450px;font-size:17.5px;font-weight:600;line-height:25px;color:#333}
  .intro-bar{left:70px;top:961px;width:3px;height:76px;background:var(--orange)}

  .svc-head{left:569px;top:636px;width:387px;height:70px;border:2px solid var(--orange);border-left-width:3px;
    border-radius:0 14px 0 0;padding:8px 0 0 16px}
  .svc-head .l1{font-size:21px;color:#333;font-weight:400;line-height:25px}
  .svc-head .l2{font-size:21px;color:var(--blue);font-weight:800;line-height:25px}

  .svc{left:569px;width:400px;height:75px}
  .svc .icon{position:absolute;left:0;top:4px;width:58px;height:58px}
  .svc .rule{position:absolute;left:70px;top:2px;width:2px;height:64px;background:var(--orange)}
  .svc h3{position:absolute;left:85px;top:0;font-size:18.5px;font-weight:700;color:var(--orange);white-space:nowrap}
  .svc p{position:absolute;left:85px;top:28px;font-size:15px;line-height:19px;color:#333;text-transform:uppercase;white-space:nowrap}
  .svc1{top:728px}.svc2{top:824px}.svc3{top:920px}

  .doc-badge{left:723px;top:995px;width:90px;height:90px;border-radius:50%;background:var(--orange);border:5px solid #f6d6aa;
    display:flex;align-items:center;justify-content:center}
  .contact{left:73px;font-size:18.5px;font-weight:700;color:var(--white);display:flex;align-items:center;gap:12px}
  .c1{top:1081px}.c2{top:1112px}.c3{top:1142px}
  .specialty{left:571px;top:1097px;width:400px;text-align:center;font-size:19.5px;font-weight:700;color:var(--white);line-height:26px;white-space:nowrap}
</style>
</head>
<body>
<div class="flyer">

  <div class="photo hero" role="img" aria-label="Photo of three colleagues working at computers in a bright office, one seated in a wheelchair, with green plants at the right"></div>

  <svg class="shapes" width="1000" height="1200" viewBox="0 0 1000 1200" aria-hidden="true">
    <polygon points="0,0 540,0 600,68 600,115 0,115" fill="#ffffff"/>
    <polygon points="0,8 40,8 12,40 0,40" fill="#eeeeee"/>
    <polygon points="500,8 560,8 600,68 540,68" fill="#f2f2f2"/>
    <rect x="0" y="0" width="1000" height="7" fill="#1c8fd0"/>
    <polygon points="560,0 1000,0 1000,68 610,68" fill="#1c8fd0"/>
    <polygon points="0,410 640,410 690,440 690,455 1000,455 1000,598 0,598" fill="#f28c1e"/>
    <polygon points="0,410 120,410 60,598 0,598" fill="#ef7d17"/>
    <polygon points="430,410 580,410 640,504 580,598 430,598 490,504" fill="#f39a2a" opacity=".55"/>
    <polygon points="620,440 760,440 700,540" fill="#f6a531" opacity=".45"/>
    <polygon points="860,455 1000,455 1000,598 940,598" fill="#ef7d17" opacity=".5"/>
    <polygon points="850,598 1000,598 1000,700 900,700" fill="#f3f3f3"/>
    <path d="M640,1046 L1000,1046 L1000,1200 L450,1200 Q560,1190 585,1110 Q605,1050 640,1046 Z" fill="#1c8fd0"/>
    <path d="M520,1200 Q600,1180 620,1110 L660,1200 Z" fill="#1878c4" opacity=".6"/>
    <path d="M0,1069 L560,1069 Q500,1160 450,1185 L0,1185 Z" fill="#f28c1e"/>
    <polygon points="0,1069 90,1069 20,1185 0,1185" fill="#ef7d17"/>
    <polygon points="400,1069 560,1069 520,1130" fill="#f6a531" opacity=".6"/>
    <rect x="0" y="1186" width="1000" height="14" fill="#1c8fd0"/>
  </svg>

  <div class="abs badge-spot"></div>

  <div class="abs brand-name">Brightpath Access Group, LLC</div>
  <div class="abs brand-tag">ADA Compliance Surveys &amp; Accessibility Solutions</div>
  <div class="abs site">www.<b>BrightpathAccessGroup</b>.example</div>

  <div class="abs headline">Are You A Business Owner OR<br>Attorney With A Client Who Is Dealing<br>With An ADA Violations Lawsuit?</div>
  <div class="abs call">
    <svg width="16" height="18" viewBox="0 0 16 18"><path d="M2 0h6l6 9-6 9H2l6-9z" fill="#fff"/></svg>
    DON’T PANIC! CALL NOW!
    <svg width="16" height="18" viewBox="0 0 16 18"><path d="M2 0h6l6 9-6 9H2l6-9z" fill="#fff"/></svg>
  </div>
  <div class="abs phone-pill">
    <div class="ring">
      <svg width="26" height="26" viewBox="0 0 24 24" fill="none" stroke="#fff" stroke-width="1.8"><path d="M5 3h3l2 5-2 1.5a11 11 0 0 0 6.5 6.5L16 14l5 2v3a2 2 0 0 1-2 2A17 17 0 0 1 3 5a2 2 0 0 1 2-2z"/><path d="M14 3a7 7 0 0 1 7 7M14 7a3 3 0 0 1 3 3"/></svg>
    </div>
    <span class="num">(619) 555-0148</span>
  </div>

  <div class="abs exp-box"></div>
  <div class="abs exp-years">10 YEARS</div>
  <div class="abs exp-of">OF EXPERIENCE</div>
  <div class="abs exp-over">Over</div>

  <div class="photo site-photo p-team" role="img" aria-label="Photo of a team in hard hats reviewing construction plans on a table"></div>
  <div class="photo site-photo p-law" role="img" aria-label="Photo of a civil code book beside a judge's gavel"></div>
  <div class="photo site-photo p-access" role="img" aria-label="Photo of a person in a wheelchair on a city sidewalk with accessibility graphics"></div>

  <div class="abs intro-bar"></div>
  <p class="abs intro">We have the answers and solutions to<br>all of your ADA compliance issues for your<br>business and/or client.</p>

  <div class="abs svc-head">
    <div class="l1">YOUR FULL-SERVICE</div>
    <div class="l2">ADA COMPLIANCE COMPANY</div>
  </div>

  <div class="abs svc svc1">
    <svg class="icon" viewBox="0 0 58 58" fill="none" stroke="#1c8fd0" stroke-width="2"><circle cx="33" cy="24" r="18"/><path d="M20 24c4-6 22-6 26 0-4 6-22 6-26 0z"/><circle cx="33" cy="24" r="4"/><path d="M20 37 6 51l3 3 14-14"/></svg>
    <div class="rule"></div>
    <h3>ON SITE SURVEY</h3>
    <p>An expert site survey<br>by Brightpath Access Group</p>
  </div>
  <div class="abs svc svc2">
    <svg class="icon" viewBox="0 0 58 58" fill="none" stroke="#1c8fd0" stroke-width="2"><circle cx="14" cy="16" r="7"/><path d="M14 5v4M14 23v4M3 16h4M21 16h4"/><path d="M24 22a10 10 0 0 1 20 0z"/><path d="M22 22h24"/><path d="M26 26a8 8 0 0 0 16 0"/><path d="M16 56c0-12 8-18 18-18s18 6 18 18z"/><path d="M34 38v18"/></svg>
    <div class="rule"></div>
    <h3>CONSTRUCTION SERVICES</h3>
    <p>Network of qualified specialty<br>contractors</p>
  </div>
  <div class="abs svc svc3">
    <svg class="icon" viewBox="0 0 58 58" fill="none" stroke="#1c8fd0" stroke-width="2"><rect x="8" y="8" width="34" height="46" rx="3"/><rect x="18" y="4" width="14" height="8" rx="2"/><path d="M14 22l3 3 5-5M14 34l3 3 5-5M14 46l3 3 5-5M26 23h10M26 35h8M26 47h6"/><circle cx="44" cy="42" r="9"/><path d="M44 37v5l3 3"/></svg>
    <div class="rule"></div>
    <h3>TRANSITION PLANS</h3>
    <p>There are three steps to<br>ADA compliance</p>
  </div>

  <div class="abs doc-badge">
    <svg width="44" height="44" viewBox="0 0 44 44" fill="none" stroke="#fff" stroke-width="2"><path d="M8 4h22l6 6v30H8z"/><path d="M14 14h14M14 20h16M14 26h10"/><circle cx="31" cy="31" r="5"/><path d="M28 35l-1 6 4-2 4 2-1-6"/></svg>
  </div>

  <div class="abs contact c1">
    <svg width="16" height="20" viewBox="0 0 16 20"><path d="M8 0a7 7 0 0 1 7 7c0 5-7 13-7 13S1 12 1 7a7 7 0 0 1 7-7z" fill="#fff"/><circle cx="8" cy="7" r="2.5" fill="#f28c1e"/></svg>
    Springfield, Ohio
  </div>
  <div class="abs contact c2">
    <svg width="18" height="14" viewBox="0 0 18 14" fill="none" stroke="#fff" stroke-width="1.5"><rect x="1" y="1" width="16" height="12"/><path d="M1 1l8 7 8-7"/></svg>
    Info@BrightpathAccessGroup.example
  </div>
  <div class="abs contact c3">
    <svg width="18" height="18" viewBox="0 0 24 24" fill="none" stroke="#fff" stroke-width="2"><path d="M5 3h3l2 5-2 1.5a11 11 0 0 0 6.5 6.5L16 14l5 2v3a2 2 0 0 1-2 2A17 17 0 0 1 3 5a2 2 0 0 1 2-2z"/></svg>
    (619) 555-0148
  </div>

  <p class="abs specialty">Specializes in ADA surveys,<br>litigation assistance, construction<br>consultation and transition plans.</p>
</div>
</body>
</html>
```